Maple Burrow Canine Massage Needs a Business Card Design

Maple Burrow Canine Massage is a new therapeutic canine massage company located in Nederland, Colorado. I need a business card design that include my logo and basic contact information.

Target Market(s)

Pet owners, veterinarians

Industry/Entity Type

Business

Contact Information for Business Card

Tessa Lindqvist, CCMT
303.581.7296
tessa@mapleburrowmassage.example
www.mapleburrowmassage.example

Colors
6c459b
886aae
b8a6cd
a64599
b768aa
d3a5cc
fbed22

Requirements
Must have
• Font should be similar to font in logo.

```html
<!DOCTYPE html>
<html lang="en">
<head>
<meta charset="utf-8">
<title>Maple Burrow Canine Massage – Business Card</title>
<link rel="stylesheet" href="https://fonts.googleapis.com/css2?family=Open+Sans:wght@400;600;700&display=swap">
<style>
  :root {
    --page-bg: #ecebef;
    --card-bg: #ffffff;
    --plum: #4a2a5a;
    --lavender: #b287c1;
    --lavender-soft: #d9c6e2;
    --gold: #f2d230;
    --ink: #1f1a22;
  }
  * { margin: 0; padding: 0; box-sizing: border-box; }
  html, body { width: 1200px; height: 1000px; overflow: hidden; }
  body {
    background: var(--page-bg);
    font-family: "Open Sans", Arial, sans-serif;
    position: relative;
  }
  .business-card {
    position: absolute;
    left: 265px;
    width: 665px;
    height: 397px;
    background: var(--card-bg);
    border-radius: 24px;
    overflow: hidden;
  }
  .business-card--first { top: 73px; }
  .business-card--second { top: 533px; }

  .brand-block {
    position: absolute;
    left: 55px;
    top: 60px;
    width: 220px;
    text-align: center;
  }
  .brand-dot {
    width: 140px;
    height: 140px;
    border-radius: 50%;
    background: var(--lavender);
    margin: 0 auto 18px;
  }
  .brand-name {
    color: var(--plum);
    font-weight: 700;
    font-size: 21px;
    line-height: 1.2;
  }

  .divider {
    position: absolute;
    left: 314px;
    top: 105px;
    width: 2px;
    height: 125px;
    background: linear-gradient(to bottom, rgba(178,135,193,0), var(--lavender-soft) 30%, var(--lavender-soft) 70%, rgba(178,135,193,0));
  }

  .holder {
    position: absolute;
    left: 350px;
    top: 110px;
    color: var(--plum);
    font-size: 21px;
    font-weight: 700;
    white-space: nowrap;
  }
  .holder .credential {
    font-size: 15px;
    font-weight: 400;
    color: var(--ink);
  }

  .contact-list {
    position: absolute;
    left: 348px;
    top: 180px;
    width: 295px;
    list-style: none;
  }
  .contact-list li {
    display: flex;
    align-items: center;
    gap: 8px;
    font-size: 14px;
    color: var(--ink);
    height: 24.5px;
    white-space: nowrap;
  }
  .contact-list svg { width: 14px; height: 14px; flex: none; }

  .wave {
    position: absolute;
    left: 0;
    bottom: 0;
    width: 665px;
    height: 397px;
  }
</style>
</head>
<body>

<section class="business-card business-card--first">
  <svg class="wave" viewBox="0 0 665 397" aria-hidden="true">
    <path d="M0,300 C150,380 300,362 450,335 S620,305 665,312 L665,397 L0,397 Z" fill="var(--lavender)"/>
    <path d="M0,302 C120,362 250,372 400,363 S600,350 665,366 L665,397 L0,397 Z" fill="var(--plum)"/>
    <path d="M0,302 C120,362 250,372 400,363 S600,350 665,366" fill="none" stroke="var(--gold)" stroke-width="3"/>
  </svg>
  <div class="brand-block">
    <div class="brand-dot"></div>
    <p class="brand-name">Maple Burrow<br>Canine Massage</p>
  </div>
  <div class="divider"></div>
  <h1 class="holder">Tessa Lindqvist<span class="credential">, CCMT</span></h1>
  <ul class="contact-list">
    <li><svg viewBox="0 0 16 16"><path d="M4 1.5l2.2 3-1.3 1.6a9 9 0 0 0 5 5l1.6-1.3 3 2.2-1.2 2.5C7.5 14.5 1.5 8.5 1.5 2.7z" fill="var(--lavender)"/></svg>303.581.7296</li>
    <li><svg viewBox="0 0 16 16"><rect x="1" y="3.5" width="14" height="9.5" rx="1" fill="var(--lavender)"/><path d="M1.5 4l6.5 5 6.5-5" fill="none" stroke="#fff" stroke-width="1.2"/></svg>tessa@mapleburrowmassage.example</li>
    <li><svg viewBox="0 0 16 16"><circle cx="8" cy="8" r="6.5" fill="none" stroke="var(--lavender)" stroke-width="1.6"/><path d="M1.5 8h13M8 1.5c-3 3.5-3 9.5 0 13M8 1.5c3 3.5 3 9.5 0 13" fill="none" stroke="var(--lavender)" stroke-width="1.2"/></svg>www.mapleburrowmassage.example</li>
  </ul>
</section>

<section class="business-card business-card--second">
  <svg class="wave" viewBox="0 0 665 397" aria-hidden="true">
    <path d="M0,300 C150,380 300,362 450,335 S620,305 665,312 L665,397 L0,397 Z" fill="var(--lavender)"/>
    <path d="M0,302 C120,362 250,372 400,363 S600,350 665,366 L665,397 L0,397 Z" fill="var(--plum)"/>
    <path d="M0,302 C120,362 250,372 400,363 S600,350 665,366" fill="none" stroke="var(--gold)" stroke-width="3"/>
  </svg>
  <div class="brand-block">
    <div class="brand-dot"></div>
    <p class="brand-name">Maple Burrow<br>Canine Massage</p>
  </div>
  <div class="divider"></div>
  <h2 class="holder">Tessa Lindqvist<span class="credential">, CCMT</span></h2>
  <ul class="contact-list">
    <li><svg viewBox="0 0 16 16"><path d="M4 1.5l2.2 3-1.3 1.6a9 9 0 0 0 5 5l1.6-1.3 3 2.2-1.2 2.5C7.5 14.5 1.5 8.5 1.5 2.7z" fill="var(--lavender)"/></svg>303.581.7296</li>
    <li><svg viewBox="0 0 16 16"><rect x="1" y="3.5" width="14" height="9.5" rx="1" fill="var(--lavender)"/><path d="M1.5 4l6.5 5 6.5-5" fill="none" stroke="#fff" stroke-width="1.2"/></svg>tessa@mapleburrowmassage.example</li>
    <li><svg viewBox="0 0 16 16"><circle cx="8" cy="8" r="6.5" fill="none" stroke="var(--lavender)" stroke-width="1.6"/><path d="M1.5 8h13M8 1.5c-3 3.5-3 9.5 0 13M8 1.5c3 3.5 3 9.5 0 13" fill="none" stroke="var(--lavender)" stroke-width="1.2"/></svg>www.mapleburrowmassage.example</li>
  </ul>
</section>

</body>
</html>
```